Business Card Design Project

We need a business card design for an existing company that we have just acquired and need to refresh and revamp to give it a fresher, more modern, and professional image.
We are a niche high end management consulting firm working with large KVM400 type companies.
Our services include commercial advisory, change management, culture development, leadership and team development, and training.
The old website for this company is www.rvl-nqe.com.au that will give you a better understanding of what this business does.
However, we have updated the logo and are changing the website as well so your design for the business card might influence how we design the website.
Our corporate colours are red and white but we also use light grey, black, and dark blue (occasionally) on our stationery.
The final design should communicate partnership, creativity, performance, insight, and change.
Updates

Some of you were having trouble viewing the original logo file.  I have now updated another file with .jpg version of logo.  Hope this helps.

Target Market(s)

We are a consultancy firm servicing Top KVM or Zenith 300 type companies.

Industry/Entity Type

Management Consulting

Requirements
Must have
• Design must have all contact information and logo on 1 side of card. Back of card should be solid colour or watermarked only - i.e. no real writing on back of card.
Cards must be scannable by those new business card scanners that store the image electronically.
Will be printing on high quality paper with matte finish so design must be high definition to allow good printing.
Card must be normal business card size (no small or 3/4 sized cards).
Nice to have
• A design that has a bit of 'movement' in it rather than look blockish and rigid. Not sure how this can be done but something that gives the card a sense of flow because our work all about integrating and synthesising the 'hard' commercial aspects with the 'soft' human (psychological) dimensions into contracts and projects.
Design should be transferrable to stationery and website to the extent possible/sensible.
Should not have
• - 'old fashioned' or 'girly' or 'comical' fonts.

- no clip art like images

- no superfluous design features that convey no real message or idea.

```html
<!DOCTYPE html>
<html lang="en">
<head>
<meta charset="utf-8">
<title>Ridgevale Value Leaders – Business Card Presentation</title>
<link href="https://fonts.googleapis.com/css2?family=Didact+Gothic&family=Marcellus&family=Marcellus+SC&display=swap" rel="stylesheet">
<style>
  :root{
    --board:#c9c9ca;
    --ink:#2b2b2b;
    --card:#38383a;
    --card-deep:#2c2c2e;
    --panel:#262628;
    --red:#c8102e;
    --red-dark:#9e0c22;
    --white:#ffffff;
    --muted:#cfcfcf;
  }
  *{box-sizing:border-box;margin:0;padding:0}
  html,body{width:1200px;height:848px;overflow:hidden}
  body{background:var(--board);font-family:"Didact Gothic",sans-serif;color:var(--ink)}
  .board{position:absolute;left:40px;top:150px;width:1120px}
  .intro{display:grid;grid-template-columns:repeat(3,1fr);column-gap:22px;font-size:16.5px;line-height:1.17;color:#333}
  .labels{display:grid;grid-template-columns:repeat(3,1fr);column-gap:18px;margin-top:36px}
  .label{font-size:16.5px;color:#333;padding-bottom:5px;border-bottom:1.5px solid #2f2f2f}
  .cards{display:grid;grid-template-columns:repeat(3,1fr);column-gap:18px;margin-top:12px}
  .card{position:relative;height:222px;background:radial-gradient(ellipse at 50% 40%,#404042 0%,var(--card) 55%,var(--card-deep) 100%);overflow:hidden;color:var(--white)}
  .card-texture{position:absolute;inset:0}
  .company{font-family:"Marcellus SC",serif;line-height:0.98;letter-spacing:.3px}
  .band{position:absolute;height:20px;border-radius:10px 0 0 10px;background:linear-gradient(90deg,var(--red) 0%,var(--red) 65%,var(--red-dark) 100%);font-family:"Marcellus",serif;color:var(--white);display:flex;align-items:center}
  .mark{position:absolute;background:var(--red);border-radius:10px}
  /* front */
  .front .company{position:absolute;left:22px;top:18px;font-size:19px}
  .front .band{left:18px;top:88px;width:270px;padding-left:9px;font-size:13px}
  .front .mark{left:260px;top:14px;width:86px;height:86px}
  .contact-panel{position:absolute;left:16px;top:127px;width:330px;height:88px;background:rgba(25,25,27,.55);border-radius:9px;padding:4px 10px;font-size:11.2px;color:var(--muted)}
  .contact-panel .who{display:flex;justify-content:space-between;align-items:baseline;border-bottom:1px solid #444;padding-bottom:3px}
  .contact-panel .name{font-family:"Marcellus SC",serif;font-size:14px;color:var(--white)}
  .contact-panel .role{font-size:10.6px;letter-spacing:.2px}
  .contact-grid{display:grid;grid-template-columns:1.1fr 1fr;margin-top:4px;line-height:1.45}
  .contact-grid b{font-weight:400;color:#9a9a9a;display:inline-block;width:14px}
  /* back 1 */
  .back1 .mark{left:50%;top:40px;width:140px;height:140px;margin-left:-70px;border-radius:16px}
  .back1 .company{position:absolute;left:0;right:0;top:188px;text-align:center;font-size:10.5px}
  /* back 2 */
  .back2 .company{position:absolute;left:33px;top:66px;font-size:22px}
  .back2 .band{left:22px;top:138px;width:240px;height:23px;padding-left:10px;font-size:15.5px}
  .back2 .mark{left:212px;top:50px;width:116px;height:116px;border-radius:13px}
</style>
</head>
<body>
<main class="board">
  <section class="intro">
    <p>All artwork are vector images, meaning they can be scaled to any size and still stay sharp and clear without losing any resolution/quality, ideal for transferring to any other medium, billboards, vehicle wraps, signage, web and other media and of course stationery.</p>
    <p>A new logo has also been developed using similar principles as your current logo, focusing on a more modern look that will appeal to a broader target market.</p>
    <p>Only two colours are used red and black which will be more cost effective when taken to print, the white is not an ink colour but the stock underneath.</p>
  </section>

  <div class="labels">
    <h2 class="label" style="font-weight:400">Front Business Card</h2>
    <h2 class="label" style="font-weight:400">Back Business Card Option 1</h2>
    <h2 class="label" style="font-weight:400">Back Business Card Option 2</h2>
  </div>

  <section class="cards">
    <article class="card front">
      <div class="card-texture" role="img" aria-label="Faint world map texture across the card"></div>
      <div class="company">Ridgevale<br>Value<br>Leaders</div>
      <div class="band">Consulting Services</div>
      <div class="mark"></div>
      <div class="contact-panel">
        <div class="who"><span class="name">Owen Tallis</span><span class="role">PARTNER - HEAD OF ADVISORY SERVICES</span></div>
        <div class="contact-grid">
          <div>
            <div><b>M</b>+61 (0)400 555 019</div>
            <div><b>P</b>+61 3 9000 4417</div>
            <div><b>F</b>+61 3 9000 4410</div>
            <div><b>E</b>owen.tallis@rvlgroup.com.au</div>
          </div>
          <div>
            <div><b>W</b>www.rvlgroup.com.au</div>
            <div><b>A</b>Level 6, 212 Harbour Ln,</div>
            <div><b></b>Melbourne, Vic 3000,</div>
            <div><b></b>Australia</div>
          </div>
        </div>
      </div>
    </article>

    <article class="card back1">
      <div class="card-texture" role="img" aria-label="Faint world map texture across the card"></div>
      <div class="mark"></div>
      <div class="company">Ridgevale Value Leaders</div>
    </article>

    <article class="card back2">
      <div class="card-texture" role="img" aria-label="Faint world map texture across the card"></div>
      <div class="company">Ridgevale<br>Value<br>Leaders</div>
      <div class="band">Consulting Services</div>
      <div class="mark"></div>
    </article>
  </section>
</main>
</body>
</html>
```